Logo Design with Business Card Project

Attractive Logo with colourful background !
I have uploaded a new image of the updated Home page with the Real Estate landing page for your reference.
We are looking for a Business card design which easily identifies us as a Video classifieds company.

Target Market(s)

20 - 35 yr old people who are connected through social media

Industry/Entity Type

Business

Logo Text

KEB DOZ AM

Logo styles of interest
Abstract Logo
Requirements
Must have
• Simple layout with striking / engaging colours
Nice to have
• Require an updated logo to go on business card / home page

```html
<!DOCTYPE html>
<html lang="en">
<head>
<meta charset="utf-8">
<title>KEB DOZ AM – Business Card</title>
<link rel="stylesheet" href="https://fonts.googleapis.com/css2?family=Open+Sans:wght@300;400;600;700&display=swap">
<style>
  :root {
    --page: #ffffff;
    --card: #1a1c1d;
    --white: #ffffff;
    --teal: #17b6b9;
    --orange: #f0821e;
    --map-light: rgba(210, 212, 214, 0.26);
    --map-dark: rgba(150, 152, 154, 0.10);
    --car-light: #f2f2f2;
    --car-dark: #8a8d90;
    --plane-light: #e4e6e8;
    --plane-dark: #9a9ea2;
  }
  * { margin: 0; padding: 0; box-sizing: border-box; }
  html, body {
    width: 1200px; height: 1000px; overflow: hidden;
    background: var(--page);
    font-family: "Open Sans", Arial, sans-serif;
  }
  .canvas { position: relative; width: 1200px; height: 1000px; }

  .card {
    position: absolute; top: 357px;
    width: 504px; height: 290px;
    background: var(--card);
    overflow: hidden;
  }
  .card--front { left: 79px; }
  .card--back { left: 609px; }

  .world-map {
    position: absolute; inset: 0;
    background: radial-gradient(ellipse 60% 55% at 50% 55%, var(--map-light), var(--map-dark) 65%, transparent 100%);
  }

  .wordmark {
    position: absolute;
    display: flex; align-items: center;
    color: var(--white);
    font-weight: 300;
    white-space: nowrap;
    letter-spacing: 0.01em;
  }
  .wordmark__square { background: var(--teal); flex: none; }
  .card--front .wordmark { left: 22px; top: 18px; font-size: 32px; gap: 8px; }
  .card--front .wordmark__square { width: 18px; height: 18px; }
  .card--back .wordmark { left: 0; width: 504px; top: 100px; justify-content: center; font-size: 56px; gap: 14px; }
  .card--back .wordmark__square { width: 32px; height: 32px; }

  .plane {
    position: absolute; left: 264px; top: 14px; width: 80px; height: 40px;
    border-radius: 40% 40% 45% 45%;
    background: linear-gradient(180deg, var(--plane-light), var(--plane-dark));
  }
  .car {
    position: absolute; left: 287px; top: 75px; width: 210px; height: 130px;
    border-radius: 45% 40% 30% 30%;
    background: linear-gradient(160deg, var(--car-light), var(--car-dark));
  }

  .tagline {
    position: absolute; left: 30px; top: 74px; width: 230px;
    text-align: center; color: var(--white);
    font-size: 16px; line-height: 21px;
  }
  .tagline__rank { color: var(--orange); font-weight: 700; }
  .tagline__product { color: var(--teal); font-weight: 700; }

  .person { position: absolute; left: 31px; top: 152px; width: 245px; }
  .person__name { color: var(--white); font-weight: 700; font-size: 23px; line-height: 30px; white-space: nowrap; }
  .person__role { color: var(--orange); font-size: 16px; line-height: 20px; text-align: right; }

  .contact {
    position: absolute; left: 327px; top: 202px;
    list-style: none; color: var(--white);
    font-size: 13.5px; line-height: 19.5px; white-space: nowrap;
  }
  .contact__label { color: var(--orange); }
  .contact__web { color: var(--orange); }
  .contact__gap { display: inline-block; width: 26px; }
</style>
</head>
<body>
<main class="canvas">

  <section class="card card--front" aria-label="Business card front">
    <div class="world-map" role="img" aria-label="Dotted world map in grey"></div>
    <div class="plane" role="img" aria-label="Passenger airplane in flight"></div>
    <div class="car" role="img" aria-label="White sports car"></div>

    <div class="wordmark">
      <span class="wordmark__name">KEB DOZ AM</span>
      <span class="wordmark__square"></span>
    </div>

    <p class="tagline">
      By and sell through the<br>
      <span class="tagline__rank">#1</span> <span class="tagline__product">Video Classifieds</span>
    </p>

    <div class="person">
      <p class="person__name">Daniel Hartwell</p>
      <p class="person__role">Managing Director</p>
    </div>

    <ul class="contact">
      <li><span class="contact__label">E:</span> daniel@kebdozam.com</li>
      <li class="contact__web">www.kebdozam.com</li>
      <li><span class="contact__label">Ph:</span> +617 5550 1834</li>
      <li><span class="contact__label">M:</span><span class="contact__gap"></span>0400 555 019</li>
    </ul>
  </section>

  <section class="card card--back" aria-label="Business card back">
    <div class="world-map" role="img" aria-label="Dotted world map in grey"></div>
    <div class="wordmark">
      <span class="wordmark__name">KEB DOZ AM</span>
      <span class="wordmark__square"></span>
    </div>
  </section>

</main>
</body>
</html>
```